Sign Front of Business

Sign for front of workshop. We want Tolvar Mechanical in same font and colour as logo then the logo after name. Would like a background colour maybe dark blue with a border.

Target Market(s)

Mining Community

Industry/Entity Type

Mechanical

Requirements
Must have
• Logo colours

```html
<!DOCTYPE html>
<html lang="en">
<head>
<meta charset="utf-8">
<title>Tolvar Mechanical – Workshop Sign Samples</title>
<link rel="stylesheet" href="https://fonts.googleapis.com/css2?family=Orbitron:wght@800&family=Montserrat:wght@400&display=swap">
<style>
  :root {
    --page-bg: #ffffff;
    --label-ink: #141a4a;
    --sign-navy: #0a005f;
    --sign-navy-deep: #0c0a4a;
    --sign-navy-glow: #1a1385;
    --frame-red: #ff0a0a;
    --name-blue: #178bf2;
    --name-chrome: #ededf0;
    --mark-white: #f4f6fa;
  }
  html, body {
    margin: 0;
    padding: 0;
    width: 1200px;
    height: 530px;
    overflow: hidden;
    background: var(--page-bg);
  }
  .sample-sheet {
    display: block;
    width: 1200px;
    height: 530px;
  }
  .sample-label {
    font-family: "Montserrat", sans-serif;
    font-weight: 400;
    font-size: 20px;
    letter-spacing: 0.5px;
    fill: var(--label-ink);
  }
  .sign-panel--flat { fill: var(--sign-navy); }
  .sign-frame {
    fill: none;
    stroke: var(--frame-red);
    stroke-width: 3;
  }
  .business-name {
    font-family: "Orbitron", sans-serif;
    font-weight: 800;
    font-size: 78px;
  }
  .business-name__lead { fill: var(--name-blue); }
  .business-name__trade { fill: var(--name-chrome); }
  .brand-mark__dot { fill: var(--mark-white); }
  .brand-mark__name {
    font-family: "Orbitron", sans-serif;
    font-weight: 800;
    font-size: 34px;
    fill: var(--mark-white);
  }
</style>
</head>
<body>
<svg class="sample-sheet" viewBox="0 0 1200 530" xmlns="http://www.w3.org/2000/svg" aria-labelledby="sheet-title">
  <title id="sheet-title">Two workshop sign samples for Tolvar Mechanical</title>
  <defs>
    <radialGradient id="navy-glow" cx="0.45" cy="0.3" r="0.75">
      <stop offset="0" stop-color="var(--sign-navy-glow)"/>
      <stop offset="1" stop-color="var(--sign-navy-deep)"/>
    </radialGradient>
  </defs>

  <!-- Sample 1: flat navy -->
  <g class="sign-sample">
    <text class="sample-label" x="82" y="67">SAMPLE 1</text>
    <rect class="sign-panel sign-panel--flat" x="75" y="89" width="1065" height="160"/>
    <rect class="sign-frame" x="88.5" y="99.5" width="1040" height="139"/>
    <text class="business-name" x="117" y="202" textLength="786" lengthAdjust="spacingAndGlyphs"><tspan class="business-name__lead">TOLVAR</tspan><tspan class="business-name__trade"> MECHANICAL</tspan></text>
    <g class="brand-mark">
      <circle class="brand-mark__dot" cx="988" cy="169" r="13"/>
      <text class="brand-mark__name" x="1010" y="182">KRT</text>
    </g>
  </g>

  <!-- Sample 2: navy with soft glow -->
  <g class="sign-sample">
    <text class="sample-label" x="79" y="325">SAMPLE 2</text>
    <rect class="sign-panel" x="75" y="337" width="1065" height="160" fill="url(#navy-glow)"/>
    <rect class="sign-frame" x="88.5" y="347.5" width="1040" height="139"/>
    <text class="business-name" x="117" y="450" textLength="786" lengthAdjust="spacingAndGlyphs"><tspan class="business-name__lead">TOLVAR</tspan><tspan class="business-name__trade"> MECHANICAL</tspan></text>
    <g class="brand-mark">
      <circle class="brand-mark__dot" cx="988" cy="417" r="13"/>
      <text class="brand-mark__name" x="1010" y="430">KRT</text>
    </g>
  </g>
</svg>
</body>
</html>
```